Modern card design needed for building development company

We are looking for a sharp modern new look for our business cards.
We are a New Zealand based company called TKV Ventures NZ LTD that specialises in subdividing large sections, housing and commercial buildings.
We have attached a photo of the current logo and would like to see it improved somehow as it looks a bit dated.
We are open to any colours.

Target Market(s)

Investors, Property buyers

Industry/Entity Type

Investment

Contact Information for Business Card

TKV VENTURES NZ LTD
www.tkvventuresnz.co.nz

Howard Pennick
Phone +64 21 843 192
Email hdpennick@fernmail.co.nz

Font styles to use
Serif
Sans Serif

Colors
0792cd
33a6d7
85cae6
6b449b
886aae
f04a50
ec1f27
f37122
f68d4d

Requirements
Must have
• Please try and make the logo more modern or if you have a similar one we would like to see it.

```html
<!DOCTYPE html>
<html lang="en">
<head>
<meta charset="utf-8">
<title>TKV Ventures NZ LTD – Business Card</title>
<link href="https://fonts.googleapis.com/css2?family=Arimo:wght@400;700&family=Raleway:wght@400&display=swap" rel="stylesheet">
<style>
  :root {
    --brand-blue: #0792cd;
    --mid-blue: #33a6d7;
    --light-blue: #85cae6;
    --paper: #ffffff;
    --backdrop-top: #aebdcd;
    --backdrop-bottom: #8fa4b9;
    --card-w: 900px;
    --card-h: 514px;
  }
  * { box-sizing: border-box; margin: 0; padding: 0; }
  html, body { width: 1200px; height: 1200px; overflow: hidden; }
  body {
    background: linear-gradient(180deg, var(--backdrop-top), var(--backdrop-bottom));
    position: relative;
    font-family: "Arimo", Arial, sans-serif;
  }
  .card {
    position: absolute;
    left: 150px;
    width: var(--card-w);
    height: var(--card-h);
    box-shadow: 0 6px 18px rgba(40, 60, 90, 0.25);
    overflow: hidden;
  }
  .card-back {
    top: 50px;
    background: var(--brand-blue);
    display: flex;
    align-items: center;
    justify-content: flex-end;
    padding-right: 70px;
  }
  .card-back .company-name {
    color: var(--paper);
    font-size: 34px;
  }
  .card-front {
    top: 636px;
    background: var(--paper);
  }
  .company-name {
    font-family: "Arimo", Arial, sans-serif;
    font-weight: 400;
    letter-spacing: 1px;
    white-space: nowrap;
  }
  .card-front .company-name {
    position: absolute;
    top: 150px;
    right: 60px;
    color: var(--brand-blue);
    font-size: 27px;
  }
  .holder-name {
    position: absolute;
    left: 96px;
    top: 226px;
    color: var(--light-blue);
    font-family: "Arimo", Arial, sans-serif;
    font-weight: 700;
    font-size: 34px;
  }
  .name-rule {
    position: absolute;
    left: 88px;
    top: 276px;
    width: 760px;
    height: 3px;
    background: var(--light-blue);
  }
  .contact-list {
    position: absolute;
    left: 60px;
    top: 300px;
    list-style: none;
    font-family: "Raleway", Arial, sans-serif;
    color: var(--brand-blue);
    font-size: 22px;
  }
  .contact-item {
    display: flex;
    align-items: center;
    height: 42px;
  }
  .contact-icon {
    width: 30px;
    height: 26px;
    margin-right: 26px;
    fill: var(--brand-blue);
  }
  .footer-bands {
    position: absolute;
    left: 0;
    bottom: 26px;
    width: 100%;
    height: 40px;
  }
  .band-dark { fill: var(--brand-blue); }
  .band-light { fill: var(--light-blue); }
</style>
</head>
<body>
  <section class="card card-back" aria-label="Card back">
    <span class="company-name">TKV VENTURES NZ LTD</span>
  </section>

  <section class="card card-front" aria-label="Card front">
    <span class="company-name">TKV VENTURES NZ LTD</span>

    <h1 class="holder-name">Howard Pennick</h1>
    <div class="name-rule"></div>

    <ul class="contact-list">
      <li class="contact-item">
        <svg class="contact-icon" viewBox="0 0 30 26" aria-hidden="true">
          <path d="M8 2c2 0 3 4 3.5 6 .3 1.3-1.8 2.3-1.5 3.5.8 2.5 2.5 4.4 5 5.5 1.2.4 2.2-1.6 3.4-1.3 2 .6 5.6 1.6 5.6 3.6 0 2-2.5 4.7-5 4.7C11 24 4 17 4 8.5 4 5.5 6 2 8 2z"/>
        </svg>
        <span>+64 21 843 192</span>
      </li>
      <li class="contact-item">
        <svg class="contact-icon" viewBox="0 0 30 26" aria-hidden="true">
          <rect x="1" y="5" width="28" height="17"/>
          <path d="M1 5 L15 15 L29 5" fill="none" stroke="#fff" stroke-width="2"/>
        </svg>
        <span>hdpennick@fernmail.co.nz</span>
      </li>
      <li class="contact-item">
        <svg class="contact-icon" viewBox="0 0 30 26" aria-hidden="true">
          <circle cx="15" cy="13" r="12"/>
          <g fill="none" stroke="#fff" stroke-width="1.5">
            <ellipse cx="15" cy="13" rx="5" ry="12"/>
            <line x1="3" y1="13" x2="27" y2="13"/>
            <line x1="15" y1="1" x2="15" y2="25"/>
            <line x1="5" y1="7" x2="25" y2="7"/>
            <line x1="5" y1="19" x2="25" y2="19"/>
          </g>
        </svg>
        <span>www.tkvventuresnz.co.nz</span>
      </li>
    </ul>

    <svg class="footer-bands" viewBox="0 0 900 40" preserveAspectRatio="none" aria-hidden="true">
      <polygon class="band-dark" points="0,0 560,0 540,40 0,40"/>
      <polygon class="band-light" points="572,0 900,0 900,40 552,40"/>
    </svg>
  </section>
</body>
</html>
```